WICKBLOOM

1. My company will allow people to buy either stock made or custom scented aromatherapy candles, lotions,soaps,body sprays, and wax melts. As there isn't a company that allows for custom oil scent mixes but me. We are just starting with the candles and the other items will be coming later.

2. My target audience is anyone who would want to buy my product. It isn't really limited due to the nature of the product I will be providing.

3. wickbloom.com is the domain name (purchased from plinkhost.com).

4. So what I really need is the shopping cart function. A fully coded shopping cart that will calculate shipping and sales tax if need be. I need the cart function to be just like every other major retailers shopping cart function. So they can click on an item they want and have it go into a shopping cart for the customer to then be able to go and pay for their goods. I also need help creating single pages for each product. So that each thing we make has a separate page with a description and an add to cart button.

5. I would like the color scheme to follow the logo I made. I would also like the logo top center of first page. I would like the quote " elevate your choices in aromatherapy products"

^. I basically need a checkout just like every other good website. A clear shipping area for them to populate, sales tax calculator, ya know everything a normal checkout has like brevona or dorvaly.com. I also have a vunta account already as well.

```html
<!DOCTYPE html>
<html lang="en">
<head>
<meta charset="utf-8">
<title>Wickbloom – Aromatherapy Candles</title>
<link href="https://fonts.googleapis.com/css2?family=Lato:wght@400;700;900&display=swap" rel="stylesheet">
<style>
:root{
  --purple:#a65bd0;
  --purple-dark:#8f46c0;
  --blue:#3aa9ee;
  --ink:#111111;
  --muted:#555555;
  --card:#f5f3f3;
  --footer:#0d0d0d;
  --white:#ffffff;
}
*{box-sizing:border-box;margin:0;padding:0}
html,body{width:1200px;height:4615px;overflow:hidden;background:var(--white)}
body{font-family:'Lato',sans-serif;color:var(--ink);position:relative}
.abs{position:absolute}
.btn{position:absolute;display:flex;align-items:center;justify-content:center;color:var(--white);font-weight:700;font-size:15px;background:var(--blue)}
.topbar{left:0;top:0;width:1200px;height:34px;background:var(--purple);color:var(--white);font-size:13px}
.topbar span{position:absolute;top:9px}
.header{left:0;top:34px;width:1200px;height:95px;background:var(--white)}
.nav a{position:absolute;top:39px;font-size:13px;color:#333;text-decoration:none}
.nav .active{background:var(--blue);color:var(--white);padding:6px 12px;top:33px;left:98px}
.logo-disc{left:467px;top:0;width:266px;height:265px;border-radius:50%;background:var(--white);display:flex;flex-direction:column;align-items:center;justify-content:center;gap:12px}
.logo-disc .mark{width:44px;height:44px;border-radius:50%;background:var(--purple)}
.logo-disc .name{font-weight:900;font-size:26px;letter-spacing:3px;color:var(--purple-dark)}
.hero{left:0;top:129px;width:1200px;height:598px;background:radial-gradient(circle at 75% 45%,#e89a3a 0%,#b0561f 30%,#5a2a14 65%,#2b1a12 100%)}
.hero h1{position:absolute;left:111px;top:180px;font-size:66px;line-height:77px;font-weight:700;color:var(--white);width:700px}
.arrow{position:absolute;width:38px;height:40px;background:#2f8fcc;display:flex;align-items:center;justify-content:center}
.section-title{position:absolute;left:0;width:1200px;text-align:center;font-size:43px;font-weight:700}
.section-title em{font-style:normal;color:var(--purple)}
.product{position:absolute;width:294px}
.product .img{height:323px;background:var(--card);position:relative}
.product .ph{position:absolute;left:77px;top:70px;width:140px;height:190px;border-radius:14px}
.product h3{text-align:center;font-size:22px;font-weight:700;margin-top:18px}
.product p{text-align:center;font-size:14px;color:var(--muted);line-height:18px;margin:10px 24px 0}
.product .price{text-align:center;font-size:23px;color:var(--purple);margin-top:14px}
.product .btn{position:relative;width:154px;height:41px;margin:14px auto 0}
.heart{position:absolute;right:18px;top:20px}
.badge{position:absolute;left:22px;top:24px;width:42px;height:42px;border-radius:50%;background:var(--purple);color:var(--white);font-size:11px;font-weight:700;display:flex;align-items:center;justify-content:center}
.about{left:0;top:2047px;width:1200px;height:570px;background:linear-gradient(120deg,#9d55c9,#a862d4 60%,#b57ee0)}
.about .photo{position:absolute;left:111px;top:57px;width:484px;height:457px;background:radial-gradient(circle at 55% 55%,#f2a248 0%,#9a4d18 35%,#3b2414 75%);}
.about h2{position:absolute;left:691px;top:66px;font-size:43px;color:var(--white)}
.about p{position:absolute;left:691px;width:395px;font-size:14.5px;line-height:22px;color:var(--white)}
.coming{left:111px;width:294px}
.coming .img{height:272px}
.coming h3{text-align:center;font-size:22px;font-weight:400;margin-top:20px}
.custom{left:47px;top:3358px;width:1106px;height:340px;background:linear-gradient(90deg,#3ea8ec,#56b7f1 50%,#3aa3e8);color:var(--white);text-align:center}
.custom h2{margin-top:66px;font-size:43px;font-weight:700;color:#eef7ff}
.custom p{margin:20px auto 0;width:680px;font-size:19px;line-height:28px}
.review{position:absolute;top:3868px;width:316px;height:224px;background:var(--white);border:1px solid #eee;box-shadow:0 2px 6px rgba(0,0,0,.06);padding:22px 24px}
.review .stars{color:#f2a21a;font-size:16px;letter-spacing:1px}
.review p{font-size:14.5px;line-height:22px;color:#444;margin-top:12px}
.review h4{font-size:17px;font-weight:400;color:#555;margin-top:20px}
.review small{display:block;font-size:12px;color:#666;margin-top:8px}
.review.featured{background:var(--purple);border-color:var(--purple)}
.review.featured p,.review.featured h4,.review.featured small{color:var(--white)}
.footer{left:0;top:4182px;width:1200px;height:433px;background:var(--footer);color:var(--white)}
.footer h4{position:absolute;top:76px;font-size:21px;font-weight:700}
.footer .col{position:absolute;top:126px;font-size:14.5px;line-height:39px}
.contact-row{position:absolute;left:455px;display:flex;gap:16px;font-size:14.5px;line-height:24px}
.social{position:absolute;top:278px;width:30px;height:30px;border-radius:6px;background:var(--white)}
.copyright{position:absolute;left:0;top:400px;width:1200px;text-align:center;font-size:13px}
</style>
</head>
<body>

<div class="abs topbar">
  <span style="left:111px">&#9742; Call Us : +1 555 014 2277</span>
  <span style="left:757px">My Account</span>
  <span style="left:860px">Cart</span>
  <span style="left:914px">Our Location</span>
  <span style="left:1021px">Contact Us</span>
</div>

<header class="abs header">
  <nav class="nav">
    <a class="active" href="#">Home</a>
    <a href="#" style="left:183px">About Us</a>
    <a href="#" style="left:273px">Shop</a>
    <a href="#" style="left:338px">Blog</a>
    <a href="#" style="left:399px">Contact Us</a>
    <a href="#" style="left:762px">Login / Register</a>
  </nav>
  <svg class="abs" style="left:900px;top:36px" width="24" height="24" viewBox="0 0 24 24" fill="none" stroke="#222" stroke-width="2"><circle cx="10" cy="10" r="7"/><path d="M15 15l6 6"/></svg>
  <svg class="abs" style="left:948px;top:36px" width="26" height="24" viewBox="0 0 24 22" fill="none" stroke="#222" stroke-width="1.8"><path d="M12 20S2 13.5 2 7.5A5 5 0 0 1 12 5a5 5 0 0 1 10 2.5C22 13.5 12 20 12 20z"/></svg>
  <svg class="abs" style="left:1000px;top:36px" width="26" height="24" viewBox="0 0 26 24" fill="none" stroke="#222" stroke-width="1.8"><path d="M1 2h4l3 13h13l3-9H7"/><circle cx="10" cy="20" r="2"/><circle cx="19" cy="20" r="2"/></svg>
  <span class="abs" style="left:1036px;top:39px;font-size:13px;color:#333">0 / $0.00</span>
</header>

<section class="abs hero" role="img" aria-label="Glowing pillar candles among dried petals">
  <h1>Elevate Your Choices In Aromatherapy Products</h1>
  <div class="btn" style="left:111px;top:444px;width:156px;height:40px">Contact Us</div>
  <div class="arrow" style="left:36px;top:279px"><svg width="12" height="14" viewBox="0 0 12 14" fill="none" stroke="#fff" stroke-width="2"><path d="M8 1L2 7l6 6"/></svg></div>
  <div class="arrow" style="left:1125px;top:279px"><svg width="12" height="14" viewBox="0 0 12 14" fill="none" stroke="#fff" stroke-width="2"><path d="M4 1l6 6-6 6"/></svg></div>
</section>

<div class="abs logo-disc">
  <div class="mark"></div>
  <div class="name">WICKBLOOM</div>
</div>

<h2 class="section-title" style="top:800px">Our <em>Products</em></h2>

<div class="product" style="left:111px;top:888px">
  <div class="img"><div class="badge">New</div><svg class="heart" width="28" height="26" viewBox="0 0 24 22" fill="none" stroke="#222" stroke-width="1.6"><path d="M12 20S2 13.5 2 7.5A5 5 0 0 1 12 5a5 5 0 0 1 10 2.5C22 13.5 12 20 12 20z"/></svg><div class="ph" role="img" aria-label="Cream pillar candles on a stone tray" style="background:linear-gradient(#f3dcc0,#d8c2a7)"></div></div>
  <h3>Stock-Made Candles</h3><p>Risus commodo viverra maecenas accumsan lacus vel facilisis.</p><div class="price">$99.00</div><div class="btn">Shop Now</div>
</div>
<div class="product" style="left:453px;top:888px">
  <div class="img" style="background:var(--white);box-shadow:0 2px 8px rgba(0,0,0,.15)"><svg class="heart" width="28" height="26" viewBox="0 0 24 22" fill="none" stroke="#222" stroke-width="1.6"><path d="M12 20S2 13.5 2 7.5A5 5 0 0 1 12 5a5 5 0 0 1 10 2.5C22 13.5 12 20 12 20z"/></svg><div class="ph" role="img" aria-label="Pink glass jar candle" style="background:linear-gradient(#fbc3d3,#ee6f98)"></div></div>
  <h3>Custom-Scented Candles</h3><p>Risus commodo viverra maecenas accumsan lacus vel facilisis.</p><div class="price">$99.00</div><div class="btn">Shop Now</div>
</div>
<div class="product" style="left:795px;top:888px">
  <div class="img"><svg class="heart" width="28" height="26" viewBox="0 0 24 22" fill="none" stroke="#222" stroke-width="1.6"><path d="M12 20S2 13.5 2 7.5A5 5 0 0 1 12 5a5 5 0 0 1 10 2.5C22 13.5 12 20 12 20z"/></svg><div class="ph" role="img" aria-label="White jar candle" style="background:linear-gradient(#fbf6ef,#e8dccd)"></div></div>
  <h3>Crystal-Infused Candles</h3><p>Risus commodo viverra maecenas accumsan lacus vel facilisis.</p><div class="price">$99.00</div><div class="btn">Shop Now</div>
</div>
<div class="product" style="left:111px;top:1445px">
  <div class="img"><svg class="heart" width="28" height="26" viewBox="0 0 24 22" fill="none" stroke="#222" stroke-width="1.6"><path d="M12 20S2 13.5 2 7.5A5 5 0 0 1 12 5a5 5 0 0 1 10 2.5C22 13.5 12 20 12 20z"/></svg><div class="ph" role="img" aria-label="Pink and violet glass candle" style="background:linear-gradient(#ef5a9c,#4a1f4e)"></div></div>
  <h3>Lorem ipsum dolor</h3><p>Risus commodo viverra maecenas accumsan lacus vel facilisis.</p><div class="price">$99.00</div><div class="btn">Shop Now</div>
</div>
<div class="product" style="left:453px;top:1445px">
  <div class="img"><svg class="heart" width="28" height="26" viewBox="0 0 24 22" fill="none" stroke="#222" stroke-width="1.6"><path d="M12 20S2 13.5 2 7.5A5 5 0 0 1 12 5a5 5 0 0 1 10 2.5C22 13.5 12 20 12 20z"/></svg><div class="ph" role="img" aria-label="Candle in a wooden bowl seen from above" style="left:62px;top:82px;width:170px;height:160px;border-radius:50%;background:radial-gradient(#fbd7a0,#d99a5a)"></div></div>
  <h3>Sed ut perspiciatis unde</h3><p>Risus commodo viverra maecenas accumsan lacus vel facilisis.</p><div class="price">$99.00</div><div class="btn">Shop Now</div>
</div>
<div class="product" style="left:795px;top:1445px">
  <div class="img"><div class="badge">10%</div><svg class="heart" width="28" height="26" viewBox="0 0 24 22" fill="none" stroke="#222" stroke-width="1.6"><path d="M12 20S2 13.5 2 7.5A5 5 0 0 1 12 5a5 5 0 0 1 10 2.5C22 13.5 12 20 12 20z"/></svg><div class="ph" role="img" aria-label="Three metallic tin candles" style="left:42px;top:105px;width:210px;height:130px;background:linear-gradient(90deg,#3a3a3a,#8b7355 50%,#c99a84)"></div></div>
  <h3>Nemo enim voluptatem</h3><p>Risus commodo viverra maecenas accumsan lacus vel facilisis.</p><div class="price">$99.00</div><div class="btn">Shop Now</div>
</div>

<section class="abs about">
  <div class="photo" role="img" aria-label="Amber jar candle with its lid"></div>
  <h2>About Us</h2>
  <p style="top:145px">Lorem ipsum dolor sit amet, consectetur adipiscing elit, sed do eiusmod tempor incididunt ut labore et dolore magna aliqua. Quis ipsum suspendisse ultrices gravida. Risus commodo viverra maecenas accumsan lacus vel facilisis.</p>
  <p style="top:267px">Sed ut perspiciatis unde omnis iste natus error sit voluptatem accusantium doloremque laudantium, totam rem aperiam, eaque ipsa quae ab illo inventore veritatis et quasi architecto beatae vitae dicta sunt explicabo. Nemo enim ipsam voluptatem quia voluptas sit aspernatur aut odit aut fugit, sed quia consequuntur magni dolores eos qui ratione voluptatem sequi nesciunt.</p>
  <div class="btn" style="left:691px;top:455px;width:154px;height:41px">Read More</div>
</section>

<h2 class="section-title" style="top:2692px">Something Amazing <em>is on the Way!</em></h2>
<p class="abs" style="left:0;top:2764px;width:1200px;text-align:center;font-size:15.5px;line-height:22px;color:#333">We're crafting the perfect aromatherapy experience—custom-scented candles, luxurious<br>lotions, and soothing wax melts. Get ready to elevate your self-care routine!</p>
<div class="btn" style="left:523px;top:2833px;width:154px;height:41px">Coming Soon!</div>

<div class="abs coming" style="top:2916px"><div class="img" role="img" aria-label="Lotion jar beside aloe leaves" style="background:linear-gradient(135deg,#dfe6df,#9cb98a 60%,#c69a6a)"></div><h3>Lotions</h3></div>
<div class="abs coming" style="left:453px;top:2916px"><div class="img" role="img" aria-label="Handmade soap bars on a wooden dish" style="background:linear-gradient(135deg,#a9a9a6,#e6ddc8 55%,#c4a27a)"></div><h3>Soaps</h3></div>
<div class="abs coming" style="left:795px;top:2916px"><div class="img" role="img" aria-label="Body spray bottle and amber jar" style="background:linear-gradient(135deg,#c9d8c8,#a6bba4 55%,#7a5a3c)"></div><h3>Body Sprays</h3></div>
<div class="abs" style="left:564px;top:3263px;width:20px;height:7px;background:var(--blue)"></div>
<div class="abs" style="left:590px;top:3263px;width:20px;height:7px;background:#111"></div>
<div class="abs" style="left:616px;top:3263px;width:20px;height:7px;background:#111"></div>

<section class="abs custom">
  <h2>Customize Your Candle – Your Scent, Your Way</h2>
  <p>Create a candle as unique as you! Choose your wax, blend up to 3 essential oils, pick your jar style, and personalize your label.</p>
  <div class="btn" style="left:447px;top:224px;width:213px;height:39px;background:var(--purple)">Customize &amp; Add to Cart</div>
</section>

<h2 class="section-title" style="top:3776px">What Our Members <em>Are Saying</em></h2>
<div class="review" style="left:111px"><div class="stars">★★★★★</div><p>Excepteur sint occaecat cupidatat non proident, sunt in culpa qui officia deserunt mollit anim id est laborum.</p><h4>Watterson</h4><small>Feb 01 2024</small></div>
<div class="review featured" style="left:442px"><div class="stars">★★★★★</div><p>Excepteur sint occaecat cupidatat non proident, sunt in culpa qui officia deserunt mollit anim id est laborum.</p><h4>Mary</h4><small>Feb 01 2024</small></div>
<div class="review" style="left:772px"><div class="stars">★★★★★</div><p>Excepteur sint occaecat cupidatat non proident, sunt in culpa qui officia deserunt mollit anim id est laborum.</p><h4>Geraldine</h4><small>Feb 01 2024</small></div>

<footer class="abs footer">
  <h4 style="left:113px">About Us</h4>
  <p class="abs" style="left:113px;top:124px;width:280px;font-size:14.5px;line-height:26px;font-weight:700">Lorem ipsum dolor sit amet, consectetur adipiscing elit, sed do eiusmod tempor incididunt ut labore et dolore magna aliqua.</p>
  <div class="social" style="left:113px;background:var(--blue)" aria-label="Social profile"></div>
  <div class="social" style="left:165px;width:22px;height:22px;top:282px" aria-label="Social profile"></div>
  <div class="social" style="left:213px;width:22px;height:22px;top:282px" aria-label="Social profile"></div>
  <div class="social" style="left:261px;width:26px;height:20px;top:283px" aria-label="Social profile"></div>

  <h4 style="left:455px">Contact Us</h4>
  <div class="contact-row" style="top:126px"><svg width="20" height="22" viewBox="0 0 20 22" fill="none" stroke="#fff" stroke-width="1.6"><path d="M10 21s7-7 7-12a7 7 0 0 0-14 0c0 5 7 12 7 12z"/><circle cx="10" cy="9" r="2.5"/></svg><span>123 Wickbloom Lane, Candle<br>Park NA 123456</span></div>
  <div class="contact-row" style="top:210px"><svg width="20" height="20" viewBox="0 0 20 20" fill="none" stroke="#fff" stroke-width="1.6"><path d="M4 2h4l2 5-3 2a11 11 0 0 0 4 4l2-3 5 2v4a2 2 0 0 1-2 2A16 16 0 0 1 2 4a2 2 0 0 1 2-2z"/></svg><span>+ 1 555 014 2277</span></div>
  <div class="contact-row" style="top:264px"><svg width="20" height="18" viewBox="0 0 20 18" fill="none" stroke="#fff" stroke-width="1.6"><rect x="1" y="2" width="18" height="14"/><path d="M1 3l9 7 9-7"/></svg><span>info@wickbloom.com</span></div>

  <h4 style="left:752px">Quick Links</h4>
  <div class="col" style="left:752px">Home<br>About Us<br>Shop<br>Coming Soon<br>Blog</div>
  <h4 style="left:976px">Other Links</h4>
  <div class="col" style="left:976px">Support<br>FAQs<br>Contact Us<br>Privacy Policy<br>Terms of Service</div>

  <p class="copyright">Copyright © 2025 Wickbloom. All rights reserved.</p>
</footer>

</body>
</html>
```